Business Card Design and Logo Needed

I need Business Cards and a Logo for my website and public speaking business which can be found at: www.kelsa-thorn.example

I'm looking for creative and unique ideas. Some business cards I've found online that I like can be found at:
http://gigplatelo.example/general/18-smokin-hot-business-card-designs/

and at

http://www.vortaplume.example/2009/04/50-creative-business-cards-of-50-graphic-designers/

```html
<!DOCTYPE html>
<html lang="en">
<head>
<meta charset="utf-8">
<title>Kelsa Thorn — Business Card</title>
<link href="https://fonts.googleapis.com/css2?family=Cinzel:wght@500;600&family=PT+Sans:wght@400&display=swap" rel="stylesheet">
<style>
  :root {
    --paper: #f4dfbb;
    --paper-light: #f7e7c9;
    --paper-shade: #ecd2a8;
    --ink: #2a0b08;
    --band: #1f0101;
    --damask-dark: #2c0304;
    --damask-mid: #4f1410;
    --damask-rose: #7a3224;
    --curl-light: #f6e3c3;
    --curl-mid: #e6c89c;
    --curl-shade: #b8936a;
    --name: #f1d9b5;
  }
  * { margin: 0; padding: 0; box-sizing: border-box; }
  html, body {
    width: 1200px; height: 721px; overflow: hidden; background: #ffffff;
  }
  .card {
    position: relative;
    width: 1200px; height: 721px;
    border-radius: 0 52px 52px 52px;
    overflow: hidden;
    background: radial-gradient(ellipse at 30% 40%, var(--paper-light) 0%, var(--paper) 55%, var(--paper-shade) 100%);
  }
  .tagline {
    position: absolute; left: 96px; top: 257px;
    font-family: "PT Sans", sans-serif; font-size: 22px; color: var(--ink);
    letter-spacing: 0.4px; white-space: nowrap;
  }
  .emblem {
    position: absolute; left: 0; top: 0; width: 1200px; height: 721px;
  }
  .name {
    position: absolute; left: 773px; top: 254px;
    font-family: "Cinzel", serif; font-size: 40px; font-weight: 600;
    color: var(--name); letter-spacing: -0.5px; white-space: nowrap;
  }
  .job-title {
    position: absolute; right: 141px; top: 302px;
    font-family: "Cinzel", serif; font-size: 21px; font-weight: 500;
    color: var(--name); white-space: nowrap;
  }
  .contact-divider {
    position: absolute; top: 549px; width: 1px; height: 94px; background: var(--ink);
  }
  .contact-item {
    position: absolute;
    font-family: "PT Sans", sans-serif; font-size: 24px; color: var(--ink);
    letter-spacing: 0.9px; white-space: nowrap; line-height: 1;
  }
  .contact-icon { position: absolute; width: 24px; height: 20px; }
  .bottom-band {
    position: absolute; left: 0; right: 0; top: 643px; bottom: 0; background: var(--band);
  }
</style>
</head>
<body>
<div class="card">
  <p class="tagline">Speaker, Philanthropist, and Author of Forthcoming Book</p>

  <svg class="emblem" viewBox="0 0 1200 721">
    <defs>
      <radialGradient id="damask" cx="50%" cy="50%" r="60%">
        <stop offset="0%" stop-color="var(--damask-rose)"/>
        <stop offset="50%" stop-color="var(--damask-mid)"/>
        <stop offset="100%" stop-color="var(--damask-dark)"/>
      </radialGradient>
      <linearGradient id="curl" x1="0" y1="1" x2="0" y2="0">
        <stop offset="0%" stop-color="var(--curl-shade)"/>
        <stop offset="35%" stop-color="var(--curl-mid)"/>
        <stop offset="75%" stop-color="var(--curl-light)"/>
        <stop offset="100%" stop-color="var(--curl-mid)"/>
      </linearGradient>
      <filter id="soft" x="-20%" y="-20%" width="140%" height="140%">
        <feGaussianBlur stdDeviation="9"/>
      </filter>
      <g id="peel">
        <path d="M24 10 Q156 26 288 10 L290 4 Q156 -36 22 4 Z" fill="#3a1a0c" opacity="0.35" filter="url(#soft)"/>
        <path d="M22 4 Q156 -34 290 4 L288 10 Q156 -4 24 10 Z" fill="url(#curl)"/>
        <path d="M24 10 Q156 -4 288 10" fill="none" stroke="var(--curl-shade)" stroke-width="1.5" opacity="0.7"/>
      </g>
    </defs>

    <path d="M926 53 L1150 275 L926 497 L706 275 Z" fill="#5a3418" opacity="0.35" filter="url(#soft)" transform="translate(4 10)"/>
    <path d="M926 53 L1150 275 L926 497 L706 275 Z" fill="url(#damask)" role="img" aria-label="Deep maroon damask pattern of diamonds and flowers"/>

    <use href="#peel" transform="translate(706 275) rotate(-45.3)"/>
    <use href="#peel" transform="translate(926 53) rotate(44.7)"/>
    <use href="#peel" transform="translate(1150 275) rotate(134.7)"/>
    <use href="#peel" transform="translate(926 497) rotate(-134.7)"/>
  </svg>

  <h1 class="name">KELSA THORN</h1>
  <p class="job-title">JOB TITLE</p>

  <svg class="contact-icon" style="left:148px;top:552px" viewBox="0 0 24 20" aria-label="Phone" role="img">
    <path d="M1 7 C6 1 18 1 23 7 L20 9 L17 7 L17 5 C14 4 10 4 7 5 L7 7 L4 9 Z" fill="var(--ink)"/>
    <rect x="5" y="9" width="14" height="10" rx="2" fill="var(--ink)"/>
    <circle cx="12" cy="14" r="2.5" fill="var(--paper)"/>
  </svg>
  <div class="contact-item" style="left:210px;top:550px">00 123.4567.890</div>

  <svg class="contact-icon" style="left:148px;top:605px" viewBox="0 0 24 20" aria-label="Mobile" role="img">
    <rect x="2" y="3" width="20" height="16" rx="2" fill="var(--ink)"/>
    <rect x="5" y="0" width="3" height="4" fill="var(--ink)"/>
    <rect x="6" y="6" width="12" height="3" fill="var(--paper)"/>
    <g fill="var(--paper)">
      <rect x="6" y="11" width="3" height="2"/><rect x="10.5" y="11" width="3" height="2"/><rect x="15" y="11" width="3" height="2"/>
      <rect x="6" y="15" width="3" height="2"/><rect x="10.5" y="15" width="3" height="2"/><rect x="15" y="15" width="3" height="2"/>
    </g>
  </svg>
  <div class="contact-item" style="left:210px;top:603px">00 123.4567.890</div>

  <div class="contact-divider" style="left:190px"></div>

  <svg class="contact-icon" style="left:455px;top:552px" viewBox="0 0 24 20" aria-label="Fax" role="img">
    <rect x="6" y="1" width="12" height="6" fill="var(--ink)"/>
    <rect x="2" y="7" width="20" height="12" rx="2" fill="var(--ink)"/>
    <rect x="6" y="10" width="12" height="2" fill="var(--paper)"/>
  </svg>
  <div class="contact-item" style="left:519px;top:550px">00 123.4567.890</div>

  <svg class="contact-icon" style="left:455px;top:606px" viewBox="0 0 24 20" aria-label="Email" role="img">
    <path d="M1 8 L12 1 L23 8 L23 19 L1 19 Z" fill="var(--ink)"/>
    <path d="M3 9 L12 15 L21 9" fill="none" stroke="var(--paper)" stroke-width="1.5"/>
  </svg>
  <div class="contact-item" style="left:519px;top:606px;font-size:21px;letter-spacing:0.2px">kelsathorn@kelsa-thorn.example</div>

  <div class="contact-divider" style="left:494px"></div>

  <div class="bottom-band"></div>
</div>
</body>
</html>
```